ZEPRILO.COM is a premium domain sales company. Our competitors are companies like vastplots.example, getparcels.example, peerwords.example. Our current site is at www.zeprilos.example.

We want to have the ability to search for domains, to highlight special offers and have some testimonials on the index page.

The logo for the site is attached.

Please be sure that the order form fits on the screen without scrolling the page. I want the entire form, including the submit button to fit without any page scrolling.

Delivered product - INDEX PAGE, ORDER FORM AND CONTENT PAGE PSDs.

Target Market(s)

Small to Medium business professionals

Industry/Entity Type

It Company

Requirements
Must have
• 1. List of domains for sale
2. Simple search box with button to run the search
3. link for advanced search
4. testimonial area. Note - this can be a small box where a different testimonial is displayed on each page load.
Nice to have
• Would like the site to have some white space. Don't want a heavily packed website. Give it an "airy" feel.

```html
<!DOCTYPE html>
<html lang="en">
<head>
<meta charset="utf-8">
<title>Zeprilo.com – Premium Domains</title>
<link href="https://fonts.googleapis.com/css2?family=Arvo:wght@700&family=Open+Sans:wght@400;600;700&family=Arimo:wght@400;700&family=Noto+Serif:ital@0;1&display=swap" rel="stylesheet">
<style>
:root{
  --green:#0a6e3d;
  --blue:#0b4c9c;
  --red:#c8103f;
  --text:#1e1e1e;
  --row-light:#f6f6f6;
  --row-dark:#e1e1e1;
  --hero-a:#8c8aa3;
  --hero-b:#c9c8d4;
  --yellow:#f6d40a;
}
*{box-sizing:border-box;margin:0;padding:0}
html,body{width:950px;height:1200px;overflow:hidden;background:#fff}
body{position:relative;font-family:"Open Sans",sans-serif;color:var(--text)}
.abs{position:absolute}

/* header */
.site-header{position:absolute;left:0;top:0;width:950px;height:92px;background:#fff;border-bottom:2px solid #999}
.brand{left:40px;top:24px;font:700 38px/1 "Open Sans",sans-serif;color:var(--green);letter-spacing:-1px;display:flex;align-items:center;gap:10px}
.brand-dot{width:16px;height:16px;border-radius:50%;background:var(--blue)}
.phone{left:370px;top:40px;font:700 21px/1 "Arimo",sans-serif;color:var(--blue);display:flex;align-items:center;gap:8px}
.main-nav{left:583px;top:0;display:flex;height:90px}
.main-nav a{width:76px;height:90px;display:flex;align-items:center;justify-content:center;font:700 13px "Arimo",sans-serif;color:#222;text-decoration:none;white-space:nowrap;background:linear-gradient(#fff,#e2e2e2);border-left:1px solid #fff;border-right:1px solid #d0d0d0}
.main-nav a:nth-child(2){width:77px}.main-nav a:nth-child(3){width:87px}.main-nav a:nth-child(4){width:96px}

/* hero */
.hero{left:0;top:93px;width:950px;height:314px;background:linear-gradient(90deg,var(--hero-a) 0%,#a8a6ba 40%,var(--hero-b) 70%,#b9b8c3 100%);overflow:hidden}
.hero-photo{position:absolute;left:418px;top:10px;width:250px;height:304px;background:radial-gradient(ellipse at 50% 40%,#e6e3e0 0%,#b9b6c0 55%,rgba(170,168,184,0) 80%)}
.hero-title{left:33px;top:68px;font:700 35px/1 "Arvo",serif;color:#fff;letter-spacing:.5px;white-space:nowrap}
.hero-sub{left:33px;top:115px;font:400 14px/15px "Open Sans",sans-serif;color:#fff;width:320px}
.search-frame{left:23px;top:160px;width:498px;height:57px;border-radius:8px;background:rgba(255,255,255,.35);border:1px solid #fff}
.search-input{position:absolute;left:10px;top:9px;width:478px;height:38px;border-radius:6px;background:#fff;border:1px solid #bbb;font:400 15px/38px "Noto Serif",serif;color:#333;padding-left:16px}
.search-go{position:absolute;right:0;top:-1px;width:62px;height:38px;border-radius:0 6px 6px 0;background:var(--red);color:#fff;font:700 22px/38px "Arvo",serif;text-align:center}
.adv-link{left:33px;top:240px;display:flex;align-items:center;gap:8px;font:italic 400 20px "Noto Serif",serif;color:#fff;text-decoration:underline;white-space:nowrap}

/* testimonial */
.testimonial{left:668px;top:131px;width:248px;height:240px}
.testimonial-card{position:absolute;inset:0;background:#fff;border:2px solid #555}
.testimonial-ribbon{position:absolute;left:95px;top:14px;width:170px;height:31px;background:var(--blue);color:#fff;font:italic 400 19px/31px "Noto Serif",serif;text-align:center;clip-path:polygon(14% 0,100% 0,100% 100%,14% 100%,0 50%)}
.testimonial-text{position:absolute;left:11px;top:66px;width:230px;font:400 14px/17px "Noto Serif",serif;color:#222}
.testimonial-site{position:absolute;left:11px;top:190px;font:italic 400 14px "Noto Serif",serif;color:var(--red)}
.testimonial-dots{left:836px;top:366px;display:flex;gap:9px}
.testimonial-dots span{width:8px;height:8px;border-radius:50%;border:1px solid #666;background:#fff}
.testimonial-dots span.on{background:var(--blue);border-color:var(--blue)}

/* listing */
.tabs{left:28px;top:436px;display:flex;gap:3px}
.tab{height:33px;border-radius:5px 5px 0 0;color:#fff;font:600 14px/33px "Open Sans",sans-serif;text-align:center}
.tab-sale{width:151px;background:var(--green)}
.tab-cat{width:171px;background:var(--blue)}
.listing{left:10px;top:468px;width:666px;height:524px;border:2px solid var(--green);border-radius:10px}
.col-head{position:absolute;top:30px;font:400 16px "Arimo",sans-serif;color:#111}
.domain-row{position:absolute;left:10px;width:644px;height:37px;border:1px solid #d6d6d6;border-radius:3px;font:400 15px/35px "Arimo",sans-serif;white-space:nowrap}
.domain-row.light{background:var(--row-light)}
.domain-row.dark{background:var(--row-dark)}
.domain-row .name{position:absolute;left:7px;display:flex;align-items:center;gap:8px;font-weight:700;color:#222}
.domain-row .cat{position:absolute;left:282px}
.domain-row .price{position:absolute;left:475px}
.domain-row .buy{position:absolute;left:570px;font:700 12px/35px "Arimo",sans-serif;color:var(--red);text-decoration:underline;white-space:nowrap}
.pager{position:absolute;top:486px;left:0;width:100%;font:400 12px "Arimo",sans-serif;color:#333;white-space:nowrap}
.pager .prev{position:absolute;left:154px;font-weight:700;text-decoration:underline}
.pager .next{position:absolute;left:495px;font-weight:700;text-decoration:underline}
.pager .pages{position:absolute;left:248px;display:flex;gap:12px}
.pager .pages b{font-weight:700}

/* sidebar */
.adv-panel{left:694px;top:438px;width:246px;height:279px;background:var(--blue);border-radius:5px;color:#fff;box-shadow:0 10px 12px -8px rgba(0,0,0,.35)}
.adv-panel h2{position:absolute;left:12px;top:12px;font:600 19px "Open Sans",sans-serif;white-space:nowrap}
.adv-panel hr{position:absolute;left:8px;top:42px;width:232px;border:0;border-top:1px solid #7fa3d6}
.adv-label{position:absolute;left:16px;font:400 14px "Noto Serif",serif}
.adv-field{position:absolute;background:#fff;height:21px}
.ext{position:absolute;left:18px;top:132px;display:flex;gap:10px;font:400 13px "Noto Serif",serif;white-space:nowrap}
.ext span{display:flex;align-items:center;gap:4px}
.ext i{width:11px;height:11px;background:#fff;border:1px solid #999;display:inline-block}
.adv-strong{position:absolute;left:16px;font:700 15px "Open Sans",sans-serif}
.adv-btn{position:absolute;left:18px;top:233px;width:110px;height:29px;border-radius:5px;background:linear-gradient(#fff36b,var(--yellow) 55%,#e6b800);color:#444;font:700 15px/27px "Open Sans",sans-serif;text-align:center;border:1px solid #d3a800}
.host-card{left:694px;top:761px;width:246px;height:231px;border:1px solid #bbb;border-radius:4px;background:linear-gradient(#d9d9d9,#fff 40%)}
.host-art{position:absolute;left:12px;top:14px;width:222px;height:130px;border-radius:6px;background:radial-gradient(ellipse at 50% 45%,#8a8f96 0%,#c3c8ce 50%,rgba(255,255,255,0) 78%)}
.host-text{position:absolute;left:0;top:164px;width:100%;text-align:center;font:400 17px/21px "Open Sans",sans-serif;color:#333}
.host-text b{color:var(--green);font-weight:700}

/* footer */
.site-footer{left:0;top:1023px;width:950px;height:177px;background:var(--green);color:#fff;text-align:center;border-top:3px solid #d8d8d8}
.foot-links{position:absolute;top:20px;width:100%;font:400 14px "Open Sans",sans-serif}
.foot-links span{margin:0 6px}
.foot-rule{position:absolute;left:94px;top:49px;width:768px;border-top:1px solid #a9cdb8}
.foot-address{position:absolute;top:64px;width:100%;font:400 15px "Open Sans",sans-serif}
.foot-contact{position:absolute;top:92px;width:100%;display:flex;justify-content:center;align-items:center;gap:12px}
.chat-badge{background:#fff;color:var(--green);border-radius:4px;padding:4px 7px;font:700 13px "Open Sans",sans-serif}
.foot-phone{font:700 30px "Open Sans",sans-serif}
.foot-copy{position:absolute;top:145px;width:100%;font:400 11px "Open Sans",sans-serif}
</style>
</head>
<body>

<header class="site-header">
  <div class="abs brand"><span>ZEPRILO.COM</span><span class="brand-dot"></span></div>
  <div class="abs phone">
    <svg width="20" height="16" viewBox="0 0 20 16"><path d="M2 5c0-3 16-3 16 0v2h-4V5H6v2H2z" fill="#666"/><rect x="4" y="8" width="12" height="7" rx="1" fill="#666"/><circle cx="10" cy="11.5" r="2" fill="#fff"/></svg>
    + 1-555-014-2290
  </div>
  <nav class="abs main-nav">
    <a>Home</a><a>FAQ's</a><a>About Us</a><a>Contact Us</a>
  </nav>
</header>

<section class="abs hero">
  <div class="hero-photo" role="img" aria-label="Photo of a smiling businessman in a suit seated at a desk with a laptop"></div>
  <h1 class="abs hero-title">Get a Domain Name</h1>
  <p class="abs hero-sub">Enter the domain name you want or multiple names separated by spaces.</p>
  <div class="abs search-frame">
    <div class="search-input">Enter your domain name here<div class="search-go">Go</div></div>
  </div>
  <a class="abs adv-link">
    <svg width="26" height="14" viewBox="0 0 26 14"><path d="M0 5h14V0l12 7-12 7V9H0z" fill="#f08a1c"/></svg>
    Advanced Search
  </a>
</section>

<aside class="abs testimonial">
  <svg class="abs" style="left:140px;top:236px" width="40" height="28" viewBox="0 0 40 28"><path d="M0 0h40L2 26z" fill="#fff" stroke="#555" stroke-width="2"/><rect x="1" y="-2" width="38" height="4" fill="#fff"/></svg>
  <div class="testimonial-card">
    <div class="testimonial-ribbon">Testimonial</div>
    <p class="testimonial-text">good service: webmaster get notice of relefant domain names:! Quick ownership and login after transaction is made. I hope they expand there service to do .eu domains also.</p>
    <p class="testimonial-site">marketlane.example</p>
  </div>
</aside>
<div class="abs testimonial-dots"><span></span><span class="on"></span><span></span><span></span></div>

<div class="abs tabs">
  <div class="tab tab-sale">Domains for Sale</div>
  <div class="tab tab-cat">Domains Categories</div>
</div>

<section class="abs listing">
  <div class="col-head" style="left:45px">Domain</div>
  <div class="col-head" style="left:305px">Category</div>
  <div class="col-head" style="left:513px">Price</div>

  <div class="domain-row light" style="top:59px"><span class="name"><svg width="16" height="10" viewBox="0 0 16 10"><path d="M0 3h9V0l7 5-7 5V7H0z" fill="none" stroke="#666"/></svg>healvora.com</span><span class="cat">Health</span><span class="price">$8700.00</span><span class="buy">Buy now</span></div>
  <div class="domain-row dark" style="top:100px"><span class="name"><svg width="16" height="10" viewBox="0 0 16 10"><path d="M0 3h9V0l7 5-7 5V7H0z" fill="none" stroke="#666"/></svg>pitchwallets.com</span><span class="cat">Sports</span><span class="price">$5000.00</span><span class="buy">Buy now</span></div>
  <div class="domain-row light" style="top:141px"><span class="name"><svg width="16" height="10" viewBox="0 0 16 10"><path d="M0 3h9V0l7 5-7 5V7H0z" fill="none" stroke="#666"/></svg>healvora.com</span><span class="cat">Health</span><span class="price">$8700.00</span><span class="buy">Buy now</span></div>
  <div class="domain-row dark" style="top:182px"><span class="name"><svg width="16" height="10" viewBox="0 0 16 10"><path d="M0 3h9V0l7 5-7 5V7H0z" fill="none" stroke="#666"/></svg>pitchwallets.com</span><span class="cat">Sports</span><span class="price">$5000.00</span><span class="buy">Buy now</span></div>
  <div class="domain-row light" style="top:223px"><span class="name"><svg width="16" height="10" viewBox="0 0 16 10"><path d="M0 3h9V0l7 5-7 5V7H0z" fill="none" stroke="#666"/></svg>healvora.com</span><span class="cat">Health</span><span class="price">$8700.00</span><span class="buy">Buy now</span></div>
  <div class="domain-row dark" style="top:264px"><span class="name"><svg width="16" height="10" viewBox="0 0 16 10"><path d="M0 3h9V0l7 5-7 5V7H0z" fill="none" stroke="#666"/></svg>pitchwallets.com</span><span class="cat">Sports</span><span class="price">$5000.00</span><span class="buy">Buy now</span></div>
  <div class="domain-row light" style="top:305px"><span class="name"><svg width="16" height="10" viewBox="0 0 16 10"><path d="M0 3h9V0l7 5-7 5V7H0z" fill="none" stroke="#666"/></svg>healvora.com</span><span class="cat">Health</span><span class="price">$8700.00</span><span class="buy">Buy now</span></div>
  <div class="domain-row dark" style="top:346px"><span class="name"><svg width="16" height="10" viewBox="0 0 16 10"><path d="M0 3h9V0l7 5-7 5V7H0z" fill="none" stroke="#666"/></svg>pitchwallets.com</span><span class="cat">Sports</span><span class="price">$5000.00</span><span class="buy">Buy now</span></div>
  <div class="domain-row light" style="top:387px"><span class="name"><svg width="16" height="10" viewBox="0 0 16 10"><path d="M0 3h9V0l7 5-7 5V7H0z" fill="none" stroke="#666"/></svg>healvora.com</span><span class="cat">Health</span><span class="price">$8700.00</span><span class="buy">Buy now</span></div>
  <div class="domain-row dark" style="top:428px"><span class="name"><svg width="16" height="10" viewBox="0 0 16 10"><path d="M0 3h9V0l7 5-7 5V7H0z" fill="none" stroke="#666"/></svg>pitchwallets.com</span><span class="cat">Sports</span><span class="price">$5000.00</span><span class="buy">Buy now</span></div>

  <div class="pager">
    <span class="prev">Previous</span>
    <span class="pages"><span>1</span><b>2</b><span>3</span><span>4</span><span>5</span><span>6</span><span>7</span><span>8</span><span>9</span><span>10</span></span>
    <span class="next">Next</span>
  </div>
</section>

<aside class="abs adv-panel">
  <h2>Advanced Search</h2>
  <hr>
  <div class="adv-label" style="top:54px">Keyword (s):</div>
  <div class="adv-field" style="left:14px;top:76px;width:218px"></div>
  <div class="adv-label" style="top:113px">Extension :</div>
  <div class="ext"><span><i></i>All</span><span><i></i>.com</span><span><i></i>.net</span><span><i></i>.org</span></div>
  <div class="adv-strong" style="top:168px">Price :</div>
  <div class="adv-field" style="left:82px;top:169px;width:70px"></div>
  <div class="adv-field" style="left:158px;top:169px;width:70px"></div>
  <div class="adv-strong" style="top:196px">Length:</div>
  <div class="adv-field" style="left:82px;top:197px;width:70px"></div>
  <div class="adv-field" style="left:158px;top:197px;width:70px"></div>
  <div class="adv-btn">Search</div>
</aside>

<aside class="abs host-card">
  <div class="host-art" role="img" aria-label="Illustration of server racks connected to several laptops around a world map"></div>
  <p class="host-text">Host your website with<br><b>Zeprilo.com</b> and<br>experience fanatical support.</p>
</aside>

<footer class="abs site-footer">
  <div class="foot-links">Home<span>|</span>FAQ's<span>|</span>About Us<span>|</span>Contact Us<span>|</span>Universal Terms<span>|</span>Refund Policy<span>|</span>Privacy Policy</div>
  <div class="foot-rule"></div>
  <div class="foot-address">(c) 2013 Zeprilo, Inc., 480 Maple Crest Road Suite 210 Fairview, OR 97024 United States</div>
  <div class="foot-contact"><span class="chat-badge">ChatDesk</span><span class="foot-phone">+1 555.014.2290</span></div>
  <div class="foot-copy">© Copyright 2013 zeprilo.com, Getparcels is a Plotmedia Property. All Rights Reserved.</div>
</footer>

</body>
</html>
```